Fahrzeugbeschriftung für einen Malerbetrieb
Zielgruppe
Malerbetrieb
Aufgabenstellung
Neue Info von meinen Kunden:
Hallo Jasper,
Danke für deine Entwürfe.
Ich hätte gerne wie in meiner ,,Kunden Idee' gesendet einen Entwurf so wie im Anhang mit kleinen Veränderungen wie unten aufgeführt.
Bitte so nah wie möglich an den Entwürfen, wie nochmal im Anhang eingefügt, diese habe ich mal mit Vorta KI gemacht.
Die Bilder entsprechen meiner Vorstellung des Designs und ich möchte gerne so wenig Abweichungen wie möglich.
Von Heckklappe und Fahrer- / Beifahrertür auf Höhe des Türgriffes, hätte ich gerne 'Maler- und Putzbetrieb' stehen. Bitte die Schrift gerade setzen, das 'Brenk' groß darunter, sodass es vom Silbernen ins bunte läuft.
Dies fehlt noch auf den Fotos. Der Strich des Buchstabens 'B' soll wie in meinem Firmenlogo langgezogen sein.
Die Handynummer kann man z.B. als Abschuss unter das 'Brenk' in die letzten Abschnitte der unteren Falz setzen.
Keine weiteren Angaben außer wie besprochen irgendwas in der Richtung 'seit über 90 Jahren' ect...(erstmal zweitrangig)
Die Adresse möchte ich auf den Seiten im Farblichen aber 'unsichtbar' (wenn das farbliche Design in Glanz ist, die Adresse nur klein in matt in gleicher Farbe darauf setzen, damit sie zwar da ist aber nicht auf ersten Blick erkennbar)

```html
<!DOCTYPE html>
<html lang="de">
<head>
<meta charset="utf-8">
<title>Brenk – Fahrzeugbeschriftung</title>
<link rel="stylesheet" href="https://fonts.googleapis.com/css2?family=Arimo:wght@400;700&family=Great+Vibes&display=swap">
<style>
  :root {
    --frame: #4a4a4a;
    --backdrop: #ececec;
    --silver: #c9cbcd;
    --wrap-dark: #2b2624;
    --logo-white: #ececec;
    --tagline: #e2cc38;
    --splash-yellow: #f3c21c;
    --splash-orange: #f08a1c;
    --splash-red: #e23b2a;
    --splash-blue: #2d4f9c;
  }
  html, body {
    margin: 0;
    padding: 0;
    width: 1200px;
    height: 1073px;
    overflow: hidden;
    background: var(--frame);
  }
  .canvas {
    position: relative;
    width: 1200px;
    height: 1073px;
    background: var(--frame);
  }
  .side-view {
    position: absolute;
    left: 0;
    width: 1200px;
    height: 494px;
    background: var(--backdrop);
  }
  .side-view--driver { top: 41px; }
  .side-view--passenger { top: 537px; }
  .side-view svg { display: block; }
  .body-panel { fill: var(--silver); }
  .wrap-dark { fill: var(--wrap-dark); }
  .brand-name {
    font-family: 'Arimo', Arial, sans-serif;
    font-weight: 700;
    font-size: 74px;
    fill: var(--logo-white);
  }
  .brand-mark { fill: var(--logo-white); }
  .brand-trade {
    font-family: 'Arimo', Arial, sans-serif;
    font-weight: 400;
    font-size: 22px;
    fill: var(--logo-white);
  }
  .tagline {
    font-family: 'Great Vibes', cursive;
    font-size: 24px;
    fill: var(--tagline);
  }
</style>
</head>
<body>
<main class="canvas">

  <section class="side-view side-view--driver" aria-label="Fahrerseite">
    <svg width="1200" height="494" viewBox="0 0 1200 494">
      <defs>
        <linearGradient id="splash-driver" x1="0" y1="1" x2="1" y2="0">
          <stop offset="0" stop-color="var(--splash-yellow)"/>
          <stop offset="0.35" stop-color="var(--splash-orange)"/>
          <stop offset="0.6" stop-color="var(--splash-red)"/>
          <stop offset="1" stop-color="var(--splash-blue)"/>
        </linearGradient>
      </defs>
      <rect class="body-panel" x="45" y="20" width="1120" height="430" rx="60"/>
      <polygon class="wrap-dark" points="1100,20 1165,60 1165,450 440,450 560,390 700,300 1050,40"/>
      <polygon role="img" aria-label="Farbspritzer-Band in Gelb, Orange, Rot und Blau" fill="url(#splash-driver)"
        points="560,385 640,250 820,170 1040,60 1110,70 1125,180 930,245 760,320 640,370"/>
      <rect class="brand-mark" x="644" y="244" width="38" height="38"/>
      <text class="brand-name" x="690" y="290">Brenk</text>
      <text class="brand-trade" x="642" y="318">Maler- und Putzbetrieb</text>
      <text class="tagline" x="960" y="262" transform="rotate(-28 960 262)">Tradition seit 90 Jahren</text>
    </svg>
  </section>

  <section class="side-view side-view--passenger" aria-label="Beifahrerseite">
    <svg width="1200" height="494" viewBox="0 0 1200 494">
      <defs>
        <linearGradient id="splash-passenger" x1="1" y1="1" x2="0" y2="0">
          <stop offset="0" stop-color="var(--splash-yellow)"/>
          <stop offset="0.35" stop-color="var(--splash-orange)"/>
          <stop offset="0.6" stop-color="var(--splash-red)"/>
          <stop offset="1" stop-color="var(--splash-blue)"/>
        </linearGradient>
      </defs>
      <rect class="body-panel" x="35" y="20" width="1120" height="430" rx="60"/>
      <polygon class="wrap-dark" points="100,20 35,60 35,450 820,450 700,390 560,300 150,40"/>
      <polygon role="img" aria-label="Farbspritzer-Band in Gelb, Orange, Rot und Blau" fill="url(#splash-passenger)"
        points="650,385 570,250 390,170 160,60 100,70 95,180 280,245 450,320 570,370"/>
      <rect class="brand-mark" x="336" y="237" width="38" height="38"/>
      <text class="brand-name" x="382" y="283">Brenk</text>
      <text class="brand-trade" x="334" y="311">Maler- und Putzbetrieb</text>
      <text class="tagline" x="100" y="180" transform="rotate(30 100 180)">Tradition seit 90 Jahren</text>
    </svg>
  </section>

</main>
</body>
</html>
```